Need Catering Menu designed - design that we want is attached

Hi,
We need a new catering menu designed for our cafe.
I have attached our coffee menu, we would like it to follow the same kind of layout.
It needs to be A4, and can be double sided.
I have attached a word doc of our catering menu, so this is what needs to be on the catering menu you produce.
Also, our contact details need to be on both sides of the menu:
Visit us instore to discuss catering options, or call 0438 672 914 or email martha@velbrisco.com.au
I have also attached our new logo which I'd like incorporated into the menu
Doctors/Nurses
Hospital staff
University Students
Catering

```html
<!DOCTYPE html>
<html lang="en">
<head>
<meta charset="utf-8">
<title>Lunch Catering Menu</title>
<link rel="stylesheet" href="https://fonts.googleapis.com/css2?family=Exo+2:wght@300;400;500;600&family=Play:wght@700&display=swap">
<style>
  :root {
    --board: #1c1c1c;
    --panel-top: #2e2e2e;
    --panel-bottom: #1a1a1a;
    --cream: #ece7a6;
    --cream-soft: #d9d3a0;
    --tan: #c8b791;
    --tan-dark: #a99770;
    --text: #e4e4e4;
    --text-dim: #cfcfcf;
  }
  * { box-sizing: border-box; margin: 0; padding: 0; }
  html, body { width: 872px; height: 1200px; overflow: hidden; background: var(--board); }
  body { font-family: "Exo 2", sans-serif; color: var(--text); position: relative; }

  .menu-frame { position: absolute; left: 12px; top: 14px; width: 848px; height: 1172px; border: 1px solid var(--cream-soft); }
  .doodle-band { position: absolute; left: 22px; top: 24px; width: 828px; height: 100px; background: linear-gradient(180deg, #d2c29c, #bba982); }
  .menu-panel { position: absolute; left: 40px; top: 92px; width: 792px; height: 1040px; background: linear-gradient(180deg, var(--panel-top) 0%, #242424 45%, var(--panel-bottom) 100%); border: 1px solid #3a3a3a; }

  .title-ribbon { position: absolute; left: 196px; top: 64px; width: 480px; height: 70px; }
  .title-ribbon h1 { position: absolute; left: 0; right: 0; top: 13px; text-align: center; font-family: "Play", sans-serif; font-size: 29px; letter-spacing: 2px; color: #f1f1f1; }

  .menu-box { position: absolute; top: 164px; height: 706px; border: 2px dotted var(--cream-soft); padding: 16px 14px; overflow: hidden; }
  .menu-box--wraps { left: 70px; width: 428px; }
  .menu-box--breads { left: 524px; width: 282px; }

  .section-head { display: flex; align-items: baseline; font-size: 18px; color: var(--cream); }
  .section-head .name { text-decoration: underline; text-underline-offset: 3px; font-weight: 500; }
  .section-head .leader { flex: 1; border-bottom: 2px dotted var(--cream); margin: 0 3px 4px; }
  .section-note { font-size: 12.5px; line-height: 1.35; color: var(--text-dim); margin-top: 2px; }
  .section-note + .section-note { margin-top: 9px; }

  .item { font-size: 12.8px; line-height: 1.3; color: var(--text-dim); margin-top: 9px; }
  .item .dish { font-size: 17px; font-weight: 500; color: var(--cream); }
  .items { margin-top: 12px; }
  .bagels { margin-top: 42px; }

  .hot-food { position: absolute; left: 68px; top: 890px; width: 726px; }
  .hot-food h2 { display: flex; align-items: center; justify-content: center; gap: 8px; font-weight: 500; font-size: 22px; color: #f4f4f4; }
  .hot-food h2::before, .hot-food h2::after { content: ""; width: 150px; border-top: 1.5px solid var(--text-dim); }
  .hot-grid { display: grid; grid-template-columns: 275px 1fr; column-gap: 30px; margin-top: 10px; }
  .hot-row { display: flex; align-items: baseline; font-size: 18.5px; font-weight: 300; color: var(--cream); height: 29px; }
  .hot-row .leader { flex: 1; border-bottom: 2px dotted var(--cream); margin: 0 6px 5px; opacity: .85; }

  .contact-bar { position: absolute; left: 0; right: 0; top: 1143px; display: flex; justify-content: center; align-items: center; gap: 10px; font-size: 16.5px; color: var(--text); }
  .contact-bar .detail { display: flex; align-items: center; gap: 6px; color: var(--cream); margin-left: 12px; }
</style>
</head>
<body>
  <div class="menu-frame"></div>
  <div class="doodle-band" role="img" aria-label="Hand-drawn café doodle pattern in beige and grey"></div>
  <div class="menu-panel"></div>

  <div class="title-ribbon">
    <svg width="480" height="70" viewBox="0 0 480 70">
      <polygon points="0,22 50,22 50,62 0,62 16,42" fill="var(--tan)"/>
      <polygon points="480,22 430,22 430,62 480,62 464,42" fill="var(--tan)"/>
      <polygon points="40,54 50,62 50,54" fill="var(--tan-dark)"/>
      <polygon points="440,54 430,62 430,54" fill="var(--tan-dark)"/>
      <rect x="40" y="2" width="400" height="52" fill="#2a2a2a" stroke="var(--tan)" stroke-width="3"/>
      <rect x="46" y="8" width="388" height="40" fill="none" stroke="var(--cream-soft)" stroke-width="1"/>
    </svg>
    <h1>LUNCH</h1>
  </div>

  <section class="menu-box menu-box--wraps">
    <div class="section-head"><span class="name">Sandwiches or Wraps</span><span class="leader"></span><span>$7.50</span></div>
    <p class="section-note">Sandwiches cut into quarters – Wraps cut into thirds</p>
    <div class="items">
      <p class="item"><span class="dish">· Ham:</span> butter, pickle spread, cheese, tomato, champagne leg ham</p>
      <p class="item"><span class="dish">· Turkey:</span> butter, cranberry sauce, lettuce mix, tomato, turkey breast</p>
      <p class="item"><span class="dish">· Sweet Chilli Chicken:</span> butter, sweet chilli sauce, aioli, lettuce mix, tomato, cheese, sweet chilli chicken tenders</p>
      <p class="item"><span class="dish">· Chicken Schnitzel:</span> butter, aioli, lettuce mix, tomato, tasty cheese, chicken schnitzel</p>
      <p class="item"><span class="dish">· Chicken and Avocado:</span> butter, aioli, lettuce mix, tomato, cheese, chicken breast, avocado</p>
      <p class="item"><span class="dish">· Egg:</span> butter, lettuce mix, egg, aioli, parsley, spring onion</p>
      <p class="item"><span class="dish">· Tuna:</span> butter, lettuce, tuna, aioli, sundried tomato, spring onion</p>
      <p class="item"><span class="dish">· B.L.T.:</span> butter, aioli, lettuce, tomato, bacon</p>
      <p class="item"><span class="dish">· Salad:</span> butter, lettuce mix, red onion, cucumber, capsicum, tomato, avocado, tasty cheese</p>
      <p class="item"><span class="dish">· Tandoori Chicken:</span> butter, tzatziki, lettuce mix, tomato, tandoori chicken</p>
      <p class="item"><span class="dish">· Waldorf Chicken:</span> butter, cos lettuce, chicken, seeded mustard, celery, walnuts, aioli</p>
      <p class="item"><span class="dish">· Chicken Ceasar:</span> butter, aioli, cos lettuce, chicken, parmesan cheese, bacon</p>
      <p class="item"><span class="dish">· Cajun Chicken:</span> butter, lettuce mix, tomato, red onion, Cajun chicken</p>
      <p class="item"><span class="dish">· Barbeque Chicken:</span> butter, BBQ &nbsp;<span class="dish">· Felafel:</span></p>
    </div>
  </section>

  <section class="menu-box menu-box--breads">
    <div class="section-head"><span class="name">Foccacias</span><span class="leader"></span><span>$8.50</span></div>
    <p class="section-note">Cut in half – please let us know if you want them toasted</p>
    <p class="section-note">** Same options as wraps and sandwiches – Plus:</p>
    <p class="item"><span class="dish">· Roast Veggie:</span> butter, pesto, grilled eggplant, grilled zucchini, roasted capsicum, feta cheese, baby spinach</p>
    <p class="item"><span class="dish">· Salami:</span> butter, pesto, baby spinach, mild salami, roasted capsicum, olives, feta cheese</p>
    <p class="item"><span class="dish">· Chicken Schnitzel:</span> Butter, Housemade coleslaw, chicken schnitzel</p>

    <div class="bagels">
      <div class="section-head"><span class="name">Bagels</span><span class="leader"></span><span>$9.00</span></div>
      <p class="section-note">Cut in half – please let us know if you want them toasted</p>
      <p class="item"><span class="dish">· Turkey:</span> cranberry sauce, baby spinach, tomato, camembert cheese</p>
      <p class="item"><span class="dish">· Smoked Salmon:</span> butter, cream cheese, baby spinach, tomato, smoked salmon</p>
    </div>
  </section>

  <section class="hot-food">
    <h2>Hot Food</h2>
    <div class="hot-grid">
      <div>
        <p class="hot-row"><span>Assorte Pies</span><span class="leader"></span><span>$5.0</span></p>
        <p class="hot-row"><span>Large tray hot chips</span><span class="leader"></span><span>$15</span></p>
        <p class="hot-row"><span>Small tray hot chips</span><span class="leader"></span><span>$9.0</span></p>
        <p class="hot-row"><span>Mini samosa</span><span class="leader"></span><span>$3.0</span></p>
        <p class="hot-row"><span>Vegetarian spring rolls</span><span class="leader"></span><span>$9.0</span></p>
        <p class="hot-row"><span>Party pies</span><span class="leader"></span><span>$3.0</span></p>
        <p class="hot-row"><span>Mini sausage rolls</span><span class="leader"></span><span>$5.0</span></p>
      </div>
      <div>
        <p class="hot-row"><span>Mini quiche</span><span class="leader"></span><span>$5.0</span></p>
        <p class="hot-row"><span>Mini dim sim</span><span class="leader"></span><span>$5.0</span></p>
        <p class="hot-row"><span>Sweet chilli chicken tenders</span><span class="leader"></span><span>$2.0</span></p>
        <p class="hot-row"><span>Meat Balls</span><span class="leader"></span><span>$3.0</span></p>
        <p class="hot-row"><span>Spinach and ricotta pastizi</span><span class="leader"></span><span>$4.5</span></p>
        <p class="hot-row"><span>Vegetarian Frittata</span><span class="leader"></span><span>$4.5</span></p>
        <p class="hot-row"><span>Meat Frittata</span><span class="leader"></span><span>$2.0</span></p>
      </div>
    </div>
  </section>

  <footer class="contact-bar">
    <span>Visit us instore to discuss catering options or:</span>
    <span class="detail">
      <svg width="22" height="22" viewBox="0 0 24 24" aria-hidden="true"><path d="M6.6 10.8a15 15 0 0 0 6.6 6.6l2.2-2.2c.3-.3.7-.4 1-.2 1.1.4 2.3.6 3.6.6.6 0 1 .4 1 1V20c0 .6-.4 1-1 1A17 17 0 0 1 3 4c0-.6.4-1 1-1h3.5c.6 0 1 .4 1 1 0 1.3.2 2.5.6 3.6.1.3 0 .7-.2 1z" fill="var(--cream)"/></svg>
      0438 672 914
    </span>
    <span class="detail">
      <svg width="22" height="20" viewBox="0 0 24 22" aria-hidden="true"><rect x="2" y="5" width="20" height="15" rx="1" fill="var(--cream)"/><path d="M2 6l10 7 10-7" fill="none" stroke="#1c1c1c" stroke-width="1.6"/></svg>
      martha@velbrisco.com.au
    </span>
  </footer>
</body>
</html>
```